Beyond The Lanterns a Tola Vire Project - Not for profit project

I am looking for a basic template to use on webnode.
The site is for a charitable organization aimed at adults and importantly children. I have attached the copy. The theme of Tola Vire ( Tola Meadow in Spanish) is our family initials and the idea is to make it fun or at least interesting. We will translate the site to Spanish also. The power of waves and the power of a Greek god like Poseidon could be a good fit in developing the idea of creating waves of positive change. BUT the Wave theme and Poseidon need to be bright colours fun and inspiring. I dont want the site to look like a fantasy novel cover. Or a display of some amazing mans body as that is not the fit. Poseidon could be illustrated version. The Kite kid drawing is something my daughter did and is fun and could work to engage , who will ultimately be the one to drive this project forward. But the “Kite Kid” is not mandatory.
I would prefer if the colors are not dark or depressing. In fact this is one of the reasons I am looking for a designer - so that the designer can find a way to present the wave theme but in a bright, uplifting tone.

I will use webnode templates so I am guessing the design would be in the form of background graphics that can be used on the webnode platform. But I need your suggestions on this ?

Target Market(s)

Anyone interested in creating a fairer world

Industry/Entity Type

Democracy

Number of Pages Required

3 page

Requirements
Must have
• Basic template -
Nice to have
• None are essential but ; Waves, Kite kid, Poisedon or other greek gods

```html
<!DOCTYPE html>
<html lang="en">
<head>
<meta charset="utf-8">
<title>Beyond The Lanterns</title>
<link href="https://fonts.googleapis.com/css2?family=Outfit:wght@400;500;600;700&family=Poppins:wght@300;400;500&display=swap" rel="stylesheet">
<style>
:root{
  --teal:#1f97a2;
  --teal-dark:#157a85;
  --ink:#111;
  --text:#555;
  --muted:#999;
  --white:#fff;
  --deep:#1d2a2c;
  --footer:#0d0d0d;
}
*{margin:0;padding:0;box-sizing:border-box}
html,body{width:1200px;height:5165px;overflow:hidden}
body{position:relative;background:var(--white);font-family:'Poppins',sans-serif;color:var(--text)}
.abs{position:absolute}
h1,h2,h3,.brand{font-family:'Outfit',sans-serif;color:var(--ink)}
.photo{position:absolute}
p{font-size:11px;line-height:18px}

/* header */
.hero-bg{left:0;top:0;width:1200px;height:600px;background:linear-gradient(180deg,#5f8e8c 0%,#8fb1ad 30%,#c7d8d4 60%,#ffffff 100%)}
.navbar{left:140px;top:26px;width:916px;height:60px;background:var(--white);box-shadow:0 4px 14px rgba(0,0,0,.08);display:flex;align-items:center}
.brand{position:absolute;left:46px;top:10px;text-align:center;font-weight:600;font-size:19px;line-height:20px}
.brand span{display:block;color:var(--teal);font-family:'Poppins',sans-serif;font-weight:400;font-size:10px;letter-spacing:4px;line-height:14px}
.menu{position:absolute;left:282px;top:22px;display:flex;gap:44px;font-size:12px;color:#222}
.menu .caret{color:var(--teal);font-size:8px}
.flag{position:absolute;left:842px;top:18px;width:28px;height:20px;border-radius:2px;overflow:hidden}
.flag i{display:block;height:5px;background:#c60b1e}
.flag b{display:block;height:10px;background:#ffc400}
.side-dots{left:49px;top:212px}
.side-dots i{display:block;width:12px;height:12px;border:1px solid #777;border-radius:50%;margin-bottom:32px}
.side-dots i.on{border-color:var(--teal);background:radial-gradient(circle,var(--teal) 3px,transparent 4px)}
.hero-title{left:0;top:178px;width:1200px;text-align:center;font-size:68px;font-weight:700;line-height:80px}
.hero-sub{left:0;top:258px;width:1200px;text-align:center;font-family:'Outfit',sans-serif;font-size:44px;color:var(--teal);font-weight:400}
.hero-text{left:400px;top:322px;width:400px;text-align:center;font-size:11px;line-height:18px;color:#444}
.btn{display:flex;align-items:center;justify-content:center;gap:22px;font-size:10px;font-weight:500}
.btn-teal{left:552px;top:388px;width:110px;height:32px;background:var(--teal);color:var(--white);border-radius:2px}
.chevron{left:588px;top:488px}

/* generic sections */
.sec-title{font-size:44px;font-weight:600;line-height:52px}
.copy p{margin-bottom:18px}
.band{left:0;width:1200px}
.teal-band{background:linear-gradient(135deg,#1b8f9b,#24a2ab 60%,#1c8c97)}
.on-dark h2{color:var(--white)}
.on-dark p{color:rgba(255,255,255,.88)}

/* focus cards */
.card-title{font-family:'Poppins',sans-serif;font-size:16px;color:#222;font-weight:400}
.card-note{border-left:3px solid var(--teal);padding-left:32px;font-size:10px;line-height:18px;color:#888}

/* blog */
.pager i{display:inline-block;width:12px;height:12px;border:1px solid #666;border-radius:50%;margin-right:32px}
.pager i.on{border-color:var(--teal);background:radial-gradient(circle,var(--teal) 3px,transparent 4px)}

/* contact */
.cta{left:248px;top:4752px;width:702px;height:210px;background:linear-gradient(120deg,#1e98a2,#137482 60%,#0e4b52);z-index:2}
.cta h2{position:absolute;left:56px;top:62px;color:var(--white);font-size:44px;font-weight:500;line-height:56px}
.btn-white{position:absolute;left:534px;top:92px;width:112px;height:32px;background:var(--white);color:var(--teal);border-radius:2px}
.footer{left:0;top:4928px;width:1200px;height:237px;background:var(--footer)}
.footer .brand{left:0;top:82px;width:1200px;color:var(--white);font-size:28px;line-height:30px}
.footer .brand span{font-size:13px;letter-spacing:6px;line-height:20px}
.social{left:542px;top:5072px;display:flex;gap:8px}
.social i{width:22px;height:22px;border-radius:50%;background:var(--teal)}
.copyright{left:0;top:5124px;width:1200px;text-align:center;font-size:10px;color:#ccc}
</style>
</head>
<body>

<!-- Header / hero -->
<div class="abs hero-bg" role="img" aria-label="Aerial view of white surf breaking over turquoise sea, fading into white"></div>
<nav class="abs navbar">
  <div class="brand">Beyond The<span>Lanterns</span></div>
  <div class="menu">
    <span>Home</span><span>Mission <span class="caret">▾</span></span><span>Who <span class="caret">▾</span></span><span>Approach</span><span>Blog</span><span>More <span class="caret">▾</span></span>
  </div>
  <div class="flag"><i></i><b></b><i></i></div>
</nav>
<div class="abs side-dots"><i></i><i></i><i class="on"></i><i></i><i></i></div>
<h1 class="abs hero-title">Beyond the Lanterns</h1>
<div class="abs hero-sub">A Tola Sea Fund</div>
<p class="abs hero-text">Never doubt that a small group of committed citizens can change the world; in fact, it is the only thing that has ever done so.</p>
<div class="abs btn btn-teal">Read More <span>›</span></div>
<svg class="abs chevron" width="24" height="24" viewBox="0 0 24 24" fill="none" stroke="#333" stroke-width="1.6"><path d="M6 5l6 6 6-6M6 12l6 6 6-6"/></svg>

<!-- Mission -->
<h2 class="abs sec-title" style="left:188px;top:684px">Mission</h2>
<div class="abs copy" style="left:188px;top:744px;width:356px">
  <p>Beyond the Lanterns champions democratic solutions for the pressing issues facing our world. These solutions must promote justice, equality, environmental responsibility, and the inherent worth of every person, in order to create a more just and equitable world for all.</p>
  <p>We advocate for robust and inclusive democracies where governments answer to the people they serve.</p>
  <p>Our goal is to counter the pursuit of political self-interest in favour of a sustainable future for both people and the planet, ensuring that no one is left behind.</p>
  <p>What counts in life is not the mere fact that we have lived. It is what difference we have made to the lives of others that will determine the significance of the life we lead.<br>Aldo Brenner</p>
</div>
<div class="photo" style="left:608px;top:664px;width:194px;height:312px;background:linear-gradient(160deg,#d9efef,#3f99b4 45%,#0f3f6b)" role="img" aria-label="Curling blue ocean wave"></div>
<div class="photo" style="left:818px;top:764px;width:194px;height:312px;background:linear-gradient(170deg,#9ec9d3,#1e6c8f 50%,#0c2f4d)" role="img" aria-label="Towering wave crashing with white spray"></div>

<!-- Who -->
<div class="abs band teal-band" style="top:1152px;height:564px"></div>
<div class="photo" style="left:188px;top:1228px;width:192px;height:292px;background:linear-gradient(180deg,#cfe0ee,#b9a58a 55%,#6fb3bf)" role="img" aria-label="Beach cove with cliffs under a cloudy sky"></div>
<div class="photo" style="left:188px;top:1536px;width:192px;height:100px;background:linear-gradient(180deg,#a8d3ea,#4aa9c4 55%,#e2d2b4)" role="img" aria-label="Sandy coastline with blue water"></div>
<div class="photo" style="left:396px;top:1228px;width:196px;height:104px;background:linear-gradient(180deg,#6b8b6a,#2f8aa3 60%,#d8c9b1)" role="img" aria-label="Green headland above a pebble beach"></div>
<div class="photo" style="left:396px;top:1348px;width:196px;height:292px;background:linear-gradient(180deg,#b7d6e8,#4f8a64 25%,#3aa6bb 50%,#dcc9a6)" role="img" aria-label="Long beach with turquoise shallows"></div>
<div class="abs on-dark copy" style="left:648px;top:1216px;width:362px">
  <h2 class="sec-title" style="margin-bottom:12px">Who</h2>
  <p>In 2023, Beyond the Lanterns - A Tola Sea Fund was brought to life by Ravi, Lenora, and Maren, driven by a mission to reshape our economy and democracy into forces that serve all, not just a privileged few.</p>
  <p>Our effort is part of a broader fight for democracy and equality that has brought about significant change around the world. Yet despite the victories, countless individuals continue to navigate life on shaky ground.</p>
  <p>Imagine if some of your friends didn't have the building blocks they needed to build their future. That wouldn't be fair, would it? We want to do our part to change that, by making sure everyone has enough blocks to build their dreams. By asking questions like "Why?" and "How can we make things better?", we want to shape a world where everyone can play, learn and live happily, with freedom and fairness as our core principles.</p>
  <p>Our lives begin to end the day we become silent about the things that matter. - Jonah Wellstead</p>
</div>

<!-- Vision -->
<h2 class="abs sec-title" style="left:188px;top:1842px">Vision</h2>
<p class="abs" style="left:188px;top:1902px;width:356px">A world where every individual, regardless of age or background, has the opportunity to thrive in a society built on the pillars of democracy, equality and sustainability. A future where our collective actions create waves of change, ensuring a fair life for all.</p>
<div class="photo" style="left:608px;top:1790px;width:404px;height:258px;background:linear-gradient(180deg,#8fb6c7,#3f7187 40%,#1a3544 75%,#0f1d25)" role="img" aria-label="Parent and child at the water's edge with rolling waves"></div>

<!-- Values -->
<div class="abs band" style="top:2124px;height:536px;background:linear-gradient(100deg,#1b1d1c 0%,#3b4644 30%,#2d6f73 60%,#1f8f97 100%)" role="img" aria-label="Dark sea cliffs with waves crashing in teal light"></div>
<div class="abs on-dark copy" style="left:608px;top:2192px;width:360px">
  <h2 class="sec-title" style="margin-bottom:6px">Values</h2>
  <p>• Kindness: The bridge that connects us all. It is the light that dissipates darkness, turning misunderstanding into harmony.</p>
  <p>• Integrity: Our compass. Doing what is right, even when it is not popular and especially when no one is watching.</p>
  <p>• Empathy: Seeing through others' eyes, embracing our differences, and finding common ground.</p>
  <p>• Love: The foundation of family and the force that transforms the ordinary into the extraordinary.</p>
  <p>• Education: Aldo Brenner said it best: "The most powerful weapon which you can use to change the world."</p>
  <p>• Curiosity: The insatiable urge to explore and understand fuels human progress, paving the way for a just world and scientific breakthroughs.</p>
</div>

<!-- Key focus -->
<h2 class="abs" style="left:0;top:2722px;width:1200px;text-align:center;font-size:44px;font-weight:600;line-height:52px">Key Focus Areas of</h2>
<div class="abs" style="left:0;top:2778px;width:1200px;text-align:center;font-family:'Outfit',sans-serif;font-size:48px;color:var(--teal);line-height:56px">Beyond the Lanterns</div>
<p class="abs" style="left:376px;top:2846px;width:448px;text-align:center;color:#444">We dream of a better world, yet we understand that dreaming alone cannot bring about change. It takes action, education, and hope to turn those dreams into reality.</p>

<div class="photo" style="left:188px;top:2948px;width:264px;height:262px;background:linear-gradient(180deg,#e4e6e6,#9aa0a2 50%,#2c2e30)" role="img" aria-label="Protester holding a sign at a rally"></div>
<div class="photo" style="left:468px;top:2948px;width:264px;height:262px;background:linear-gradient(180deg,#1c1c1c,#5a4a2e 55%,#2a2418)" role="img" aria-label="Small figures standing on stacks of coins"></div>
<div class="photo" style="left:746px;top:2948px;width:266px;height:262px;background:linear-gradient(180deg,#c4d7e6,#7b8a6e 45%,#2f3c58)" role="img" aria-label="Crowd gathered at a street demonstration"></div>
<div class="abs card-title" style="left:188px;top:3230px">Democracy and Equality</div>
<div class="abs card-title" style="left:468px;top:3230px">Economic Inclusion</div>
<div class="abs card-title" style="left:746px;top:3230px">Education</div>
<div class="abs card-note" style="left:164px;top:3282px;width:270px">Freedom and opportunity are precious gifts and the purpose of good democracy is to expand them for all people. We believe pillars of good democracy rest firmly on the foundations of equality.</div>
<div class="abs card-note" style="left:468px;top:3282px;width:230px">Would you play a game where not everyone has the chance to score? That is the economic field for many. Beyond the Lanterns is committed to contributing to changing that game.</div>
<div class="abs card-note" style="left:746px;top:3282px;width:270px">Education is the key that unlocks change. Yet, not everyone has access to this key. We believe in a world where every child and adult has the chance to explore, learn, and grow.</div>

<!-- Specifics -->
<div class="abs band" style="top:3456px;height:474px;background:linear-gradient(100deg,#3a3f3e 0%,#2f4a4b 35%,#1d7f88 65%,#1f97a2 100%)" role="img" aria-label="Stormy waves crashing on dark rocks"></div>
<div class="abs on-dark copy" style="left:662px;top:3520px;width:352px">
  <h2 class="sec-title" style="margin-bottom:6px">Specifics of our Support</h2>
  <p>Beyond the Lanterns supports charities and not for profits that promote:</p>
  <p>Democracy - projects and organizations working to strengthen the foundations of democracy.</p>
  <p>Equality - projects and organizations combating the unequal distribution of opportunities across the social, economic, political, and cultural spheres.</p>
  <p>Education - initiatives that broaden the availability of education.</p>
</div>

<!-- Blog -->
<h2 class="abs" style="left:0;top:3990px;width:1200px;text-align:center;font-size:44px;font-weight:600;line-height:52px">Latest Posts In</h2>
<div class="abs" style="left:0;top:4046px;width:1200px;text-align:center;font-family:'Outfit',sans-serif;font-size:48px;color:var(--teal);line-height:56px">Our Blog</div>
<p class="abs" style="left:0;top:4118px;width:1200px;text-align:center;color:#333;font-size:10px">Be the first to read what's new!</p>
<svg class="abs" style="left:188px;top:4180px" width="194" height="244" role="img" aria-label="Person in a shawl on a grey beach"><defs><linearGradient id="gb1" x1="0" y1="0" x2="0" y2="1"><stop offset="0" stop-color="#9aa3a6"/><stop offset="1" stop-color="#3d4a55"/></linearGradient></defs><polygon points="0,0 194,12 194,232 0,244" fill="url(#gb1)"/></svg>
<div class="photo" style="left:396px;top:4170px;width:406px;height:268px;background:linear-gradient(160deg,#b8c7cc,#5e7f8f 40%,#1f3a4c 75%,#2d5566)" role="img" aria-label="Sea stacks beyond a black sand beach in blue mist"></div>
<svg class="abs" style="left:818px;top:4180px" width="194" height="244" role="img" aria-label="Surfer leaping in grey light"><defs><linearGradient id="gb2" x1="0" y1="0" x2="0" y2="1"><stop offset="0" stop-color="#8d8d8d"/><stop offset="1" stop-color="#2a2a2a"/></linearGradient></defs><polygon points="0,12 194,0 194,244 0,232" fill="url(#gb2)"/></svg>
<div class="abs" style="left:0;top:4470px;width:1200px;text-align:center;font-size:10px;color:var(--teal)">25/04/2024</div>
<div class="abs" style="left:0;top:4492px;width:1200px;text-align:center;font-size:19px;line-height:26px;color:#222">Blog Post With<br>Formatting Tips For You</div>
<p class="abs" style="left:0;top:4556px;width:1200px;text-align:center;font-size:10px;color:#444">Use headings to divide your content</p>
<svg class="abs" style="left:584px;top:4596px" width="32" height="32" viewBox="0 0 32 32"><circle cx="16" cy="16" r="15" fill="var(--teal)"/><path d="M12 20l8-8M14 12h6v6" stroke="#fff" stroke-width="1.5" fill="none"/></svg>
<div class="abs pager" style="left:506px;top:4660px"><i></i><i></i><i class="on"></i><i></i><i></i></div>

<!-- Footer + contact -->
<div class="abs footer">
  <div class="brand">Beyond The<span>Lanterns</span></div>
</div>
<div class="abs cta">
  <h2>Do You Need To<br>Contact Us?</h2>
  <div class="btn btn-white">Read More <span>›</span></div>
</div>
<div class="abs social"><i></i><i></i><i></i><i></i></div>
<div class="abs copyright">© 2024 Orin Pell. 48 Harbor Lane, Portvale, PV 20417</div>

</body>
</html>
```